Vexor Mind Social Media Advertisement

We need a social media advertisement made up for our Asset Insight. Our initial campaign will be on Reddit, so it needs to be compliant with reddit. Attached is a brief, we just need 1 single design initially that we can interchange the copy to see what converts better. Must be in a format that we can easily edit. Attached also are some examples of advertisements that are currently posted on Reddit for similar products. Coinsprig is the closest competitor. Please visit our website: https://www.vexormind.example to understand more about the business. You can also register as a free user to view the platform.

Target Market(s)

Self-directed Australian investors — particularly Self managed super fund trustees and property investors — who actively manage their own wealth and want AI-powered insights to make smarter financial decisions.

Industry/Entity Type

Financial technology (FinTech) / Wealth management software.

Requirements
Must have
• Dark, sophisticated colour palette (navy and teal), no emoji or decorative icons, clean and modern typography, and imagery that conveys intelligence, data, and financial confidence — not generic stock market clichés.
Nice to have
• Subtle futuristic or tech aesthetic, data visualisation elements (charts, graphs, network nodes), a sense of calm authority rather than aggressive "get rich" energy, and designs that would work across both digital ads and print formats.
Should not have
• Bright or garish colours, cartoonish illustrations, generic stock market imagery (bulls, bears, ticker tape), cluttered layouts, anything that feels salesy or hype-driven, and no cryptocurrency or "get rich quick" visual cues.

```html
<!DOCTYPE html>
<html lang="en">
<head>
<meta charset="utf-8">
<title>Vexor Mind — See Exactly When You Can Retire</title>
<link href="https://fonts.googleapis.com/css2?family=Plus+Jakarta+Sans:wght@500;600;700;800&family=Inter:wght@400;500;600;700&display=swap" rel="stylesheet">
<style>
  :root{
    --bg:#0e1920;
    --bg-deep:#0a1217;
    --grid:rgba(120,170,190,0.05);
    --panel:#0d1318;
    --card:#111a20;
    --card-line:#1f2c35;
    --text:#ffffff;
    --muted:#8b98a3;
    --dim:#5d6b76;
    --teal:#2dd4bf;
    --teal-btn:#33d1b3;
    --blue:#4aa3e6;
    --blue-btn:#3b82f6;
    --ink:#0b1a1f;
    --orange:#f0a21a;
    --green:#34d399;
  }
  *{box-sizing:border-box;margin:0;padding:0}
  html,body{width:1200px;height:1200px;overflow:hidden;background:var(--bg)}
  body{font-family:"Inter",sans-serif;color:var(--text)}
  .canvas{position:relative;width:1200px;height:1200px;overflow:hidden;
    background:
      linear-gradient(var(--grid) 1px,transparent 1px) 0 0/60px 60px,
      linear-gradient(90deg,var(--grid) 1px,transparent 1px) 0 0/60px 60px,
      radial-gradient(ellipse at 50% 35%,#132530 0%,var(--bg) 60%,var(--bg-deep) 100%);}
  .stage{position:absolute;left:0;top:0;width:1080px;height:1080px;transform:scale(1.11111);transform-origin:0 0}
  .abs{position:absolute}

  .brand{left:0;width:1080px;top:42px;text-align:center;font-family:"Plus Jakarta Sans",sans-serif;font-weight:700;font-size:34px;letter-spacing:-0.5px;color:var(--text)}
  .headline{left:0;width:1080px;top:120px;text-align:center;font-family:"Plus Jakarta Sans",sans-serif;font-weight:800;font-size:94px;line-height:102px;letter-spacing:-2px}
  .headline .accent{background:linear-gradient(90deg,#2fd9b8 0%,#3cc3d4 50%,#4f9fe8 100%);-webkit-background-clip:text;background-clip:text;color:transparent}
  .pillars{left:225px;top:335px;width:632px;height:78px;border:2px solid var(--teal);border-radius:10px;display:flex;align-items:center;justify-content:center;gap:62px;font-family:"Inter",sans-serif;font-size:31px;color:#a9b4bd;box-shadow:0 0 18px rgba(45,212,191,0.25)}
  .pillars span{display:flex;align-items:center;gap:12px}
  .pillars span::before{content:"";width:12px;height:12px;border-radius:50%;background:var(--teal)}
  .cta{left:437px;top:470px;width:206px;height:59px;border-radius:6px;background:var(--teal-btn);color:var(--ink);font-family:"Plus Jakarta Sans",sans-serif;font-weight:600;font-size:19px;display:flex;align-items:center;justify-content:center;box-shadow:0 0 24px rgba(51,209,179,0.35)}

  /* side screens */
  .screen{background:var(--panel);border:1px solid #23404a;border-radius:12px;overflow:hidden;font-size:7px;color:var(--muted)}
  .frame{border:2px solid rgba(45,212,191,0.55);border-radius:16px;box-shadow:0 0 30px rgba(45,212,191,0.25)}
  .feed{left:22px;top:688px;width:200px;height:420px}
  .scenario{left:858px;top:688px;width:200px;height:420px}
  .feed-frame{left:14px;top:680px;width:216px;height:440px}
  .scen-frame{left:850px;top:680px;width:216px;height:440px}
  .t{position:absolute;white-space:nowrap}
  .b{color:var(--text);font-weight:600}

  /* main portfolio */
  .main-frame{left:195px;top:578px;width:690px;height:540px;background:#0f1c22}
  .main{left:205px;top:588px;width:670px;height:520px;background:var(--panel);border:1px solid #22313a;border-radius:10px;overflow:hidden;font-size:7px;color:var(--muted)}
  .topbar{position:absolute;left:0;top:0;width:100%;height:24px;border-bottom:1px solid var(--card-line)}
  .btn{position:absolute;height:18px;border-radius:4px;display:flex;align-items:center;justify-content:center;font-size:7px}
  .btn-ghost{border:1px solid #2d3a44;color:#c8d0d6}
  .btn-sync{background:var(--blue-btn);color:#fff}
  .tabs{position:absolute;left:15px;top:79px;display:flex;gap:5px}
  .tab{height:15px;padding:0 9px;border:1px solid #2b3943;border-radius:8px;display:flex;align-items:center;font-size:7px;color:#aab4bc}
  .tab.active{border-color:var(--teal);color:var(--teal)}
  .stat{position:absolute;top:105px;width:155px;height:52px;background:var(--card);border:1px solid var(--card-line);border-radius:6px}
  .stat .lbl{position:absolute;left:9px;top:10px;font-size:6px;letter-spacing:.4px;color:var(--muted)}
  .stat .val{position:absolute;left:9px;top:20px;font-size:12px;font-weight:600;color:var(--text)}
  .stat .sub{position:absolute;left:9px;top:37px;font-size:6px;color:var(--green)}
  .stat .ico{position:absolute;right:9px;top:11px;width:16px;height:16px;border-radius:4px}
  .box{position:absolute;background:var(--card);border:1px solid var(--card-line);border-radius:6px}
  .row{position:absolute;left:115px;height:10px;width:295px;font-size:6.5px}
  .row .dot{position:absolute;left:0;top:2px;width:5px;height:5px;border-radius:50%}
  .row .tk{position:absolute;left:9px;top:0;color:#dbe2e7;font-weight:600}
  .row .track{position:absolute;left:38px;top:4px;width:230px;height:2px;background:#1e2a32;border-radius:1px}
  .row .fill{position:absolute;left:0;top:0;height:2px;border-radius:1px}
  .row .pct{position:absolute;right:0;top:0;color:#c2cad0}
  .pos{position:absolute;width:208px;height:75px;background:var(--card);border:1px solid var(--card-line);border-radius:6px}
  .pos .tk{position:absolute;left:9px;top:10px;font-size:9px;font-weight:700;color:var(--text)}
  .pos .nm{position:absolute;left:9px;top:24px;font-size:7px;color:#aeb8bf}
  .pos .sh{position:absolute;left:9px;top:36px;font-size:6px;color:var(--dim)}
  .pos .pr{position:absolute;right:9px;top:10px;font-size:9px;font-weight:700;color:var(--text)}
  .pos .gn{position:absolute;right:9px;top:24px;font-size:6.5px;color:var(--green)}
  .pos .cl{position:absolute;left:9px;top:51px;font-size:6px;color:var(--dim)}
  .pos .cp{position:absolute;right:9px;top:51px;font-size:6px;color:#c2cad0}
  .pos .bar{position:absolute;left:9px;right:9px;top:61px;height:2px;background:#1e2a32}
  .pos .bar i{position:absolute;left:0;top:0;height:2px}
  .advisor{position:absolute;background:#0f1a20;border:1px solid #2b4a52;border-radius:6px;padding:7px 8px;font-size:6px;color:#aeb8bf;line-height:9px}
  .advisor strong{display:block;color:var(--text);font-size:7px;margin-bottom:3px}
  .fab{position:absolute;width:28px;height:28px;border-radius:50%;background:var(--teal-btn);border:2px solid #0b1a1f}
</style>
</head>
<body>
<div class="canvas">
<div class="stage">

  <div class="abs brand">Vexor Mind</div>
  <h1 class="abs headline">See Exactly When<br><span class="accent">You Can Retire.</span></h1>
  <div class="abs pillars"><span>Model it.</span><span>Track it.</span><span>Own it.</span></div>
  <div class="abs cta">Explore Platform</div>

  <!-- intelligence feed screen -->
  <div class="abs frame feed-frame"></div>
  <div class="abs screen feed">
    <div class="t b" style="left:12px;top:12px;font-size:7px">≡&nbsp;&nbsp;Intelligence</div>
    <div style="position:absolute;left:0;top:26px;width:100%;border-top:1px solid var(--card-line)"></div>
    <div class="t b" style="left:14px;top:37px;font-size:10px">Intelligence Feed</div>
    <div class="t" style="left:14px;top:51px;font-size:6px">Earnings · Insider trades · Competitive moves · Management</div>
    <div class="t" style="left:14px;top:67px;font-size:6.5px;color:#dbe2e7">Feed 63&nbsp;&nbsp;&nbsp;&nbsp;&nbsp;Signals&nbsp;&nbsp;&nbsp;&nbsp;&nbsp;Growth Scanner</div>
    <div style="position:absolute;left:14px;top:78px;width:30px;height:1px;background:var(--orange)"></div>
    <div style="position:absolute;left:14px;top:87px;width:180px;height:66px;border:1px solid #3a3320;border-radius:5px;background:#14181a"></div>
    <div class="t" style="left:20px;top:92px;font-size:5.5px;color:var(--orange)">TODAY'S DIGEST — SUNDAY 22 MARCH</div>
    <div class="t b" style="left:20px;top:104px;font-size:7px">Coastal LNG Restart Lifts GLF; RDG Export Di</div>
    <div class="t" style="left:20px;top:116px;font-size:5.5px;line-height:8px">Energy names rallied on supply news and revised<br>value targets. Miners face near-term demand risk as<br>board succession plans come into focus this year.</div>
    <div class="t" style="left:14px;top:172px;font-size:6px">▽ &nbsp;All assets ▾&nbsp;&nbsp;&nbsp;All categories&nbsp;&nbsp;&nbsp;Earnings</div>
    <div class="t" style="left:14px;top:192px;font-size:6px;color:#dbe2e7">Feed 63&nbsp;&nbsp;&nbsp;&nbsp;Saved 0</div>
    <div style="position:absolute;left:14px;top:202px;width:180px;border-top:1px solid var(--card-line)"></div>
    <div style="position:absolute;left:22px;top:214px;width:16px;height:16px;border-radius:4px;background:#1c2830"></div>
    <div class="t b" style="left:46px;top:214px;font-size:7px">VLTA <span style="color:var(--green);font-weight:500">● Bullish</span> <span style="color:var(--orange);font-weight:500">● Alert</span></div>
    <div class="t" style="left:46px;top:226px;font-size:5.5px">7 updates · 22 Mar 2026 · Competitive</div>
    <div class="t b" style="left:40px;top:246px;font-size:6.5px">Revenue Visibility Through 2027 Signals Extend</div>
    <div class="t" style="left:40px;top:256px;font-size:5.5px;line-height:8px">The chief executive said the flagship platform is<br>dispelling concerns that capital spending will pe</div>
    <div class="t" style="left:40px;top:276px;font-size:5px;color:var(--dim)">20 Mar · Market Desk · <span style="color:var(--green)">Positive</span></div>
    <div class="t b" style="left:40px;top:297px;font-size:6.5px">Custom Silicon Push by Hyperscalers Gaining Mome</div>
    <div class="t" style="left:40px;top:307px;font-size:5.5px;line-height:8px">Custom chip shipments from cloud providers are proj<br>increasingly invest in their own silicon. This trend pose<br>large order commitments provide near-term buffer.</div>
    <div class="t" style="left:40px;top:335px;font-size:5px;color:var(--dim)">21 Mar · Market Desk · <span style="color:#f87171">Negative</span></div>
    <div class="t b" style="left:40px;top:352px;font-size:6.5px">Aster &amp; Corva-Based NPX System Expand AI Inf</div>
    <div class="t" style="left:40px;top:362px;font-size:5.5px;line-height:8px">Voltara's revenue disclosure was complemented by<br>inference. The NPX platform's synergy with Aster<br>beyond training accelerators strengthens long-term</div>
  </div>

  <!-- scenario screen -->
  <div class="abs frame scen-frame"></div>
  <div class="abs screen scenario">
    <div style="position:absolute;left:40px;top:35px;width:76px;height:14px;border:1px solid #2b3943;border-radius:4px"></div>
    <div style="position:absolute;left:92px;top:35px;width:58px;height:14px;background:#17303a;border:1px solid #2b4a52;border-radius:4px;font-size:6px;color:#dbe2e7;display:flex;align-items:center;justify-content:center">Scenario builder</div>
    <div class="t" style="left:160px;top:39px;font-size:6px;color:#dbe2e7">Compare</div>
    <div style="position:absolute;left:138px;top:67px;width:58px;height:11px;border:1px solid #6b5316;background:#2a2110;border-radius:3px;font-size:5.5px;color:var(--orange);display:flex;align-items:center;justify-content:center">On track to retire</div>
    <div class="t" style="left:40px;top:100px;font-size:5px;color:var(--dim)">Projected net worth</div>
    <svg style="position:absolute;left:0;top:96px" width="200" height="130" viewBox="0 0 200 130">
      <path d="M0 110 C60 100 120 70 200 20 L200 118 L0 118Z" fill="#1e3a5f" opacity=".8"/>
      <path d="M0 112 C60 104 120 82 200 45 L200 118 L0 118Z" fill="#27496f" opacity=".8"/>
      <path d="M0 114 C60 110 120 96 200 72 L200 118 L0 118Z" fill="#1a4b57" opacity=".9"/>
      <path d="M0 110 C60 100 120 70 200 20" stroke="#5a8fd6" stroke-width="1" fill="none"/>
      <line x1="0" y1="118" x2="200" y2="118" stroke="#22313a"/>
    </svg>
    <div class="t" style="left:10px;top:220px;font-size:5.5px"><span style="color:var(--orange)">L home)</span>&nbsp;&nbsp;<span style="color:var(--green)">■</span> Personal savings pool (simulated)&nbsp;&nbsp;<span style="color:#5a8fd6">■</span> Super&nbsp;&nbsp;— Total</div>
    <div class="t" style="left:10px;top:245px;font-size:5.5px;line-height:8px;color:var(--dim)">balance is shown as a simulated pool — it is not your portfolio.<br>Personal savings grow from your current balance and<br>assume steady contributions for your full retirement.</div>
    <div style="position:absolute;left:10px;top:285px;width:180px;height:120px;border:1px solid var(--card-line);border-radius:5px"></div>
    <div class="t" style="left:16px;top:292px;font-size:5.5px">Runway of fund</div>
    <svg style="position:absolute;left:10px;top:300px" width="180" height="100" viewBox="0 0 180 100">
      <path d="M0 80 C50 78 100 70 180 50" stroke="var(--teal)" stroke-width="1.2" fill="none"/>
    </svg>
    <div class="advisor" style="left:114px;top:313px;width:78px"><strong>◆ AI Advisor</strong>Ask a financial goal — get personalised strategies based on your actual numbers.</div>
  </div>

  <!-- portfolio screen -->
  <div class="abs frame main-frame"></div>
  <div class="abs main">
    <div class="topbar">
      <div class="t b" style="left:10px;top:8px;font-size:7px"><span style="color:var(--muted)">≡</span>&nbsp;&nbsp;&nbsp;Portfolio</div>
      <div class="t" style="right:12px;top:8px;font-size:6.5px"><span style="color:#aeb8bf">♪</span>&nbsp;&nbsp;&nbsp;<span style="color:var(--green)">●</span> Live</div>
    </div>
    <div class="t b" style="left:15px;top:40px;font-size:12px">Portfolio</div>
    <div class="t" style="left:15px;top:56px;font-size:6.5px">12 positions · 1 account</div>
    <div class="btn btn-ghost" style="left:516px;top:44px;width:88px">↥&nbsp; Upload Statement</div>
    <div class="btn btn-sync" style="left:609px;top:44px;width:44px">⟳&nbsp; Sync</div>
    <div class="tabs">
      <div class="tab active">Portfolio Overview</div>
      <div class="tab">Thesis</div>
      <div class="tab">Superannuation</div>
      <div class="tab">Portfolio Health</div>
      <div class="tab">Personal Shares&nbsp;<span style="background:#1e2a32;border-radius:4px;padding:0 4px">12</span></div>
    </div>
    <div class="stat" style="left:15px"><div class="lbl">TOTAL VALUE</div><div class="val">$300,954</div><div class="ico" style="background:#1e3a8a"></div></div>
    <div class="stat" style="left:176px"><div class="lbl">COST BASIS</div><div class="val">$144,695</div><div class="ico" style="background:#1e2a32"></div></div>
    <div class="stat" style="left:338px"><div class="lbl">UNREALISED GAIN</div><div class="val">$156,259</div><div class="sub">+108.0%</div><div class="ico" style="background:#124a3a"></div></div>
    <div class="stat" style="left:499px"><div class="lbl">POSITIONS</div><div class="val">12</div><div class="sub" style="color:var(--muted)">No alerts</div><div class="ico" style="background:#123c40"></div></div>

    <div class="box" style="left:15px;top:170px;width:420px;height:170px">
      <div class="t b" style="left:10px;top:11px;font-size:7px">◷&nbsp; Concentration</div>
      <svg style="position:absolute;left:12px;top:52px" width="84" height="84" viewBox="0 0 84 84" role="img" aria-label="Portfolio concentration donut chart">
        <g transform="rotate(-90 42 42)" fill="none" stroke-width="14">
          <circle cx="42" cy="42" r="32" pathLength="100" stroke="#e6a11b" stroke-dasharray="41.1 58.9" stroke-dashoffset="0"/>
          <circle cx="42" cy="42" r="32" pathLength="100" stroke="#34d399" stroke-dasharray="9.7 90.3" stroke-dashoffset="-41.1"/>
          <circle cx="42" cy="42" r="32" pathLength="100" stroke="#4ade80" stroke-dasharray="9.7 90.3" stroke-dashoffset="-50.8"/>
          <circle cx="42" cy="42" r="32" pathLength="100" stroke="#facc15" stroke-dasharray="6.7 93.3" stroke-dashoffset="-60.5"/>
          <circle cx="42" cy="42" r="32" pathLength="100" stroke="#f87171" stroke-dasharray="6.3 93.7" stroke-dashoffset="-67.2"/>
          <circle cx="42" cy="42" r="32" pathLength="100" stroke="#a78bfa" stroke-dasharray="6.3 93.7" stroke-dashoffset="-73.5"/>
          <circle cx="42" cy="42" r="32" pathLength="100" stroke="#f472b6" stroke-dasharray="4.7 95.3" stroke-dashoffset="-79.8"/>
          <circle cx="42" cy="42" r="32" pathLength="100" stroke="#60a5fa" stroke-dasharray="4.0 96" stroke-dashoffset="-84.5"/>
          <circle cx="42" cy="42" r="32" pathLength="100" stroke="#22d3ee" stroke-dasharray="3.1 96.9" stroke-dashoffset="-88.5"/>
          <circle cx="42" cy="42" r="32" pathLength="100" stroke="#fb923c" stroke-dasharray="3.0 97" stroke-dashoffset="-91.6"/>
          <circle cx="42" cy="42" r="32" pathLength="100" stroke="#c084fc" stroke-dasharray="2.7 97.3" stroke-dashoffset="-94.6"/>
          <circle cx="42" cy="42" r="32" pathLength="100" stroke="#eab308" stroke-dasharray="2.7 97.3" stroke-dashoffset="-97.3"/>
        </g>
      </svg>
      <div class="row" style="top:29px"><i class="dot" style="background:#e6a11b"></i><span class="tk">QNTX</span><span class="track"><i class="fill" style="width:95px;background:#e6a11b"></i></span><span class="pct" style="color:var(--orange)">41.1%</span></div>
      <div class="row" style="top:40px"><i class="dot" style="background:#34d399"></i><span class="tk">VLTA</span><span class="track"><i class="fill" style="width:22px;background:#34d399"></i></span><span class="pct">9.7%</span></div>
      <div class="row" style="top:51px"><i class="dot" style="background:#4ade80"></i><span class="tk">SBK.AX</span><span class="track"><i class="fill" style="width:22px;background:#4ade80"></i></span><span class="pct">9.7%</span></div>
      <div class="row" style="top:62px"><i class="dot" style="background:#facc15"></i><span class="tk">HLX.AX</span><span class="track"><i class="fill" style="width:15px;background:#facc15"></i></span><span class="pct">6.7%</span></div>
      <div class="row" style="top:73px"><i class="dot" style="background:#f87171"></i><span class="tk">NMBR</span><span class="track"><i class="fill" style="width:14px;background:#f87171"></i></span><span class="pct">6.3%</span></div>
      <div class="row" style="top:84px"><i class="dot" style="background:#a78bfa"></i><span class="tk">RDG.AX</span><span class="track"><i class="fill" style="width:14px;background:#a78bfa"></i></span><span class="pct">6.3%</span></div>
      <div class="row" style="top:95px"><i class="dot" style="background:#f472b6"></i><span class="tk">LDG.AX</span><span class="track"><i class="fill" style="width:11px;background:#f472b6"></i></span><span class="pct">4.7%</span></div>
      <div class="row" style="top:106px"><i class="dot" style="background:#60a5fa"></i><span class="tk">HRB.AX</span><span class="track"><i class="fill" style="width:9px;background:#60a5fa"></i></span><span class="pct">4.0%</span></div>
      <div class="row" style="top:117px"><i class="dot" style="background:#22d3ee"></i><span class="tk">DWL.AX</span><span class="track"><i class="fill" style="width:7px;background:#22d3ee"></i></span><span class="pct">3.1%</span></div>
      <div class="row" style="top:128px"><i class="dot" style="background:#fb923c"></i><span class="tk">CST.AX</span><span class="track"><i class="fill" style="width:7px;background:#fb923c"></i></span><span class="pct">3.0%</span></div>
      <div class="row" style="top:139px"><i class="dot" style="background:#c084fc"></i><span class="tk">GLF.AX</span><span class="track"><i class="fill" style="width:6px;background:#c084fc"></i></span><span class="pct">2.7%</span></div>
      <div class="row" style="top:150px"><i class="dot" style="background:#eab308"></i><span class="tk">ORBX</span><span class="track"><i class="fill" style="width:6px;background:#eab308"></i></span><span class="pct">2.7%</span></div>
    </div>

    <div class="box" style="left:443px;top:170px;width:210px;height:170px">
      <div class="t b" style="left:10px;top:11px;font-size:7px"><span style="color:var(--orange)">△</span>&nbsp; Alerts</div>
      <div class="t" style="left:10px;top:27px;font-size:6.5px"><span style="color:var(--green)">✓</span>&nbsp; No active alerts</div>
    </div>

    <div class="t" style="left:15px;top:352px;font-size:6.5px;letter-spacing:.5px">USER UNKNOWN</div>
    <div style="position:absolute;left:90px;top:356px;width:460px;border-top:1px solid var(--card-line)"></div>
    <div class="t" style="right:17px;top:352px;font-size:7px;color:#dbe2e7">$300,954</div>

    <div class="pos" style="left:15px;top:367px"><span class="tk">QNTX</span><span class="nm">Quantix Systems</span><span class="sh">580 shares · avg $18.40 &nbsp;✎ Edit</span><span class="pr">$123,672</span><span class="gn">↗ +$108,570 (+718.9%)</span><span class="cl">Concentration</span><span class="cp" style="color:var(--orange)">41.1%</span><span class="bar"><i style="width:41%;background:var(--orange)"></i></span></div>
    <div class="pos" style="left:231px;top:367px"><span class="tk">VLTA</span><span class="nm">Voltara Corporation</span><span class="sh">120 shares · avg $48.20 &nbsp;✎ Edit</span><span class="pr">$29,327</span><span class="gn">↗ +$21,142 (+258.3%)</span><span class="cl">Concentration</span><span class="cp">9.7%</span><span class="bar"><i style="width:10%;background:var(--blue)"></i></span></div>
    <div class="pos" style="left:446px;top:367px"><span class="tk">SBK.AX</span><span class="nm">Southern Bank of Australia</span><span class="sh">185 shares · avg A$92.40 &nbsp;✎ Edit</span><span class="pr">$29,267</span><span class="gn" style="color:var(--muted)">↗ — (+%)</span><span class="cl">Concentration</span><span class="bar"><i style="width:10%;background:var(--blue)"></i></span></div>
    <div class="pos" style="left:15px;top:447px"><span class="tk">HLX.AX</span><span class="nm">Helix Biotherapies</span><span class="sh">68 shares · avg A$268.50 &nbsp;✎ Edit</span><span class="pr">$20,101</span><span class="gn" style="color:var(--muted)">↗ — (+%)</span></div>
    <div class="pos" style="left:231px;top:447px"><span class="tk">NMBR</span><span class="nm">Nimbra Software</span><span class="sh">35 shares · avg $320.80 &nbsp;✎ Edit</span><span class="pr">$18,913</span><span class="gn">↗ +$3,025 (+19.0%)</span></div>
    <div class="pos" style="left:446px;top:447px"><span class="tk">RDG.AX</span><span class="nm">Redgum Resources</span><span class="sh">420 shares · avg A$43.20 &nbsp;✎ Edit</span><span class="pr">$18,</span><span class="gn" style="color:var(--muted)">— (+%)</span></div>

    <div class="advisor" style="left:532px;top:398px;width:122px"><strong>◆ AI Advisor</strong>Ask a financial goal — get personalised strategies based on your actual numbers.</div>
    <div class="fab" style="left:626px;top:454px"></div>
  </div>

</div>
</div>
</body>
</html>
```